Kid's Cancer Camp Business Card

Create a unique Two-Sided color business cards for Camp Willow Brook, a pediatric cancer camp.

The camp tag line is: Where every young camper finds summer joy...

Dale Morrisey, Executive Director
Camp Willow Brook Charitable Foundation, Inc
PO Box 918
Harlow Falls, NH 06832

Phone - 203-555-0143
Fax - 203-555-0187
Email: dale@campwillowbrook.example
www.campwillowbrook.example

Target Market(s)

Potential Donors, Volunteers and Campers

Industry/Entity Type

Non-profit pediatric cancer camp

Contact Information for Business Card

All contact info that is included in the description

Font styles to use
Other font styles liked:
• Designer chooses font

Requirements
Must have
• Camp Willow Brook Logo and Tag Line
Nice to have
• should be eye catching
Should not have
• not cartoony

```html
<!DOCTYPE html>
<html lang="en">
<head>
<meta charset="utf-8">
<title>Camp Willow Brook – Business Card</title>
<link href="https://fonts.googleapis.com/css2?family=Montserrat:wght@400;500;600;800&display=swap" rel="stylesheet">
<style>
  :root {
    --stage: #2b2b2b;
    --paper: #ffffff;
    --sun: #fbb429;
    --teal: #05a6a0;
    --navy: #1b5f95;
    --ink: #1a1a1a;
  }
  * { box-sizing: border-box; margin: 0; padding: 0; }
  html, body { width: 1200px; height: 689px; overflow: hidden; }
  body {
    background: var(--stage);
    font-family: "Montserrat", sans-serif;
    color: var(--ink);
    position: relative;
  }
  .card {
    position: absolute;
    top: 190px;
    width: 540px;
    height: 309px;
    background: var(--paper);
    border-radius: 18px;
    overflow: hidden;
  }
  .card--front { left: 40px; }
  .card--back { left: 620px; }

  .wordmark {
    display: flex;
    align-items: center;
    gap: 14px;
    color: var(--navy);
    font-weight: 600;
    line-height: 1.05;
    text-transform: lowercase;
  }
  .wordmark__dot {
    border-radius: 50%;
    background: var(--sun);
    flex: none;
  }
  .card--front .wordmark {
    position: absolute;
    left: 50%; top: 50%;
    transform: translate(-50%, -50%);
    font-size: 40px;
  }
  .card--front .wordmark__dot { width: 70px; height: 70px; }

  .card--back .wordmark {
    position: absolute;
    left: 22px; top: 92px;
    width: 170px;
    font-size: 20px;
    gap: 10px;
  }
  .card--back .wordmark__dot { width: 34px; height: 34px; }

  .divider {
    position: absolute;
    left: 200px; top: 34px;
    width: 1.5px; height: 172px;
    background: var(--sun);
  }
  .details {
    position: absolute;
    left: 215px; top: 30px;
    width: 310px;
  }
  .person__name {
    font-size: 19px;
    font-weight: 800;
    letter-spacing: 0.3px;
    text-transform: uppercase;
  }
  .person__first { color: var(--sun); }
  .person__last { color: var(--teal); }
  .person__role { font-size: 11px; font-weight: 500; margin-top: 2px; }
  .org { margin-top: 9px; font-size: 10.5px; line-height: 1.4; font-weight: 500; }
  .contacts { list-style: none; margin-top: 9px; }
  .contacts li {
    display: flex; align-items: center; gap: 8px;
    font-size: 10.5px; font-weight: 500; height: 15.5px;
  }
  .contacts svg { width: 11px; height: 11px; flex: none; fill: var(--sun); }

  .wave { position: absolute; left: 0; top: 0; width: 540px; height: 309px; }
</style>
</head>
<body>

<section class="card card--front">
  <div class="wordmark">
    <span class="wordmark__dot"></span>
    <span>camp<br>willow brook</span>
  </div>
</section>

<section class="card card--back">
  <svg class="wave" viewBox="0 0 540 309" aria-hidden="true">
    <path d="M0 258 C200 266 390 250 540 212 L540 309 L0 309 Z" fill="var(--teal)"/>
    <path d="M70 252 C250 248 410 232 530 200" fill="none" stroke="var(--sun)" stroke-width="3" stroke-linecap="round"/>
  </svg>

  <div class="wordmark">
    <span class="wordmark__dot"></span>
    <span>camp<br>willow brook</span>
  </div>

  <div class="divider"></div>

  <div class="details">
    <h1 class="person__name"><span class="person__first">Dale</span> <span class="person__last">Morrisey</span></h1>
    <p class="person__role">Executive Director</p>
    <p class="org">Where every young camper finds summer joy<br>Camp Willow Brook Charitable Foundation, Inc</p>
    <ul class="contacts">
      <li><svg viewBox="0 0 12 12"><path d="M2 1h2.5l1 3-1.5 1a7 7 0 0 0 3 3l1-1.5 3 1V10a1 1 0 0 1-1 1A9 9 0 0 1 1 2a1 1 0 0 1 1-1z"/></svg>203-555-0143</li>
      <li><svg viewBox="0 0 12 12"><path d="M3 1h6v3H3zM1 5h10v5H9V8H3v2H1zM3 9h6v2H3z"/></svg>203-555-0187</li>
      <li><svg viewBox="0 0 12 12"><path d="M1 2.5h10v7H1z M1.5 3l4.5 3.5L10.5 3" stroke="#fff" stroke-width="0.8"/></svg>dale@campwillowbrook.example</li>
      <li><svg viewBox="0 0 12 12"><circle cx="6" cy="6" r="5"/><path d="M1 6h10M6 1c-2.5 3-2.5 7 0 10M6 1c2.5 3 2.5 7 0 10" stroke="#fff" stroke-width="0.7" fill="none"/></svg>www.campwillowbrook.example</li>
      <li><svg viewBox="0 0 12 12"><path d="M6 0.5a4 4 0 0 1 4 4c0 3-4 7-4 7s-4-4-4-7a4 4 0 0 1 4-4z"/><circle cx="6" cy="4.5" r="1.4" fill="#fff"/></svg>PO Box 918, Harlow Falls, NH 06832</li>
    </ul>
  </div>
</section>

</body>
</html>
```